Design four banner ads for our upcoming revamped website

We need four banner ads for our website.

The link of our website is http://beta.mivarquo.com/

The banners will appear under the "Promotions" tab which is currently exhibiting placeholder images.

The titles for each of the banner ads are as follow:
1) Double Credit Chance
2) Capital Protection Scheme
3) Trade Bonus
4) 2.5% Annual Interest

Target Market(s)

forex traders

Requirements
Must have
• The banners must adhere and blend with the website existing theme
Should not have
• Please do not use any human figures in the banner or pictures of humans waving around cash.

```html
<!DOCTYPE html>
<html lang="en">
<head>
<meta charset="utf-8">
<title>Mivarquo Promotions Banners</title>
<link rel="stylesheet" href="https://fonts.googleapis.com/css2?family=Arimo:wght@700&display=swap">
<style>
  :root {
    --page: #ffffff;
    --frame: #d4d4d4;
    --orange: #f5821f;
    --orange-dark: #d8650e;
    --fold-brown: #7a3c0c;
    --navy: #3b5670;
    --ink: #ffffff;
    --photo-family-a: #c9ccd3;
    --photo-family-b: #6d7d92;
    --photo-gold-a: #f7e27a;
    --photo-gold-b: #3f9a3a;
    --photo-cash-a: #f1ece4;
    --photo-cash-b: #b1862c;
    --photo-chart-a: #f4f4f4;
    --photo-chart-b: #9aa3ad;
  }
  html, body {
    margin: 0;
    padding: 0;
    width: 933px;
    height: 1200px;
    overflow: hidden;
    background: var(--page);
  }
  .promotions {
    position: relative;
    width: 933px;
    height: 1200px;
  }
  .banner {
    position: absolute;
    left: 170px;
    width: 594px;
    height: 257px;
    background: var(--page);
    outline: 1px solid var(--frame);
    overflow: hidden;
  }
  .banner--credit { top: 24px; }
  .banner--protection { top: 301px; }
  .banner--bonus { top: 577px; }
  .banner--interest { top: 852px; }

  .banner__photo {
    position: absolute;
    inset: 0;
  }
  .banner--credit .banner__photo {
    background: linear-gradient(120deg, var(--photo-family-a), var(--photo-family-b));
    clip-path: polygon(0 0, 63% 0, 74% 100%, 0 100%);
  }
  .banner--protection .banner__photo {
    background: radial-gradient(ellipse at 22% 55%, var(--photo-gold-a) 0%, #e3b93a 35%, var(--photo-gold-b) 62%, #ffffff 80%);
    clip-path: polygon(0 0, 45% 0, 45% 100%, 0 100%);
  }
  .banner--bonus .banner__photo {
    background: linear-gradient(110deg, var(--photo-cash-a), var(--photo-cash-b) 55%, #c04a5c);
    clip-path: polygon(0 0, 62% 0, 43% 100%, 0 100%);
  }
  .banner--interest .banner__photo {
    background: linear-gradient(100deg, var(--photo-chart-a), var(--photo-chart-b));
    clip-path: polygon(0 0, 64% 0, 57% 100%, 0 100%);
  }

  .banner__art {
    position: absolute;
    inset: 0;
    width: 594px;
    height: 257px;
  }
  .shape-orange { fill: var(--orange); }
  .shape-fold { fill: var(--fold-brown); }
  .shape-fold-light { fill: var(--orange-dark); }
  .shape-navy { fill: var(--navy); }

  .headline {
    font-family: "Arimo", Arial, sans-serif;
    font-weight: 700;
    fill: var(--ink);
    text-transform: uppercase;
  }
</style>
</head>
<body>
<main class="promotions">

  <section class="banner banner--credit" aria-label="Double Credit Chance">
    <svg class="banner__art" viewBox="0 0 420 182" aria-hidden="true" focusable="false">
      <polygon class="shape-fold" points="385,28 420,52 420,132 385,153"/>
    </svg>
    <div class="banner__photo" role="img" aria-label="Photo of friends relaxing on a sofa looking at a tablet"></div>
    <svg class="banner__art" viewBox="0 0 420 182">
      <polygon class="shape-fold" points="383,28 420,52 420,132 383,153"/>
      <rect class="shape-orange" x="185" y="28" width="200" height="125"/>
      <text class="headline" x="198" y="66" font-size="20">Get Double</text>
      <text class="headline" x="198" y="89" font-size="20">Credit</text>
      <text class="headline" x="198" y="112" font-size="20">Everyday</text>
    </svg>
  </section>

  <section class="banner banner--protection" aria-label="Capital Protection Scheme">
    <div class="banner__photo" role="img" aria-label="Stacks of gold coins under a green umbrella"></div>
    <svg class="banner__art" viewBox="0 0 420 182">
      <polygon class="shape-navy" points="272,0 420,0 420,182 198,182"/>
      <polygon class="shape-fold-light" points="335,118 380,118 405,175 335,148"/>
      <polygon class="shape-orange" points="185,18 380,18 375,118 185,118"/>
      <text class="headline" x="202" y="55" font-size="18">Protect the</text>
      <text class="headline" x="202" y="75" font-size="18">Capital of</text>
      <text class="headline" x="202" y="95" font-size="18">Yours on</text>
      <text class="headline" x="202" y="115" font-size="18">Easy Way</text>
    </svg>
  </section>

  <section class="banner banner--bonus" aria-label="Trade Bonus">
    <div class="banner__photo" role="img" aria-label="Hand holding banknotes beside a bonus seal, a calculator and a notebook"></div>
    <svg class="banner__art" viewBox="0 0 420 182">
      <polygon class="shape-navy" points="260,0 420,0 420,182 180,182"/>
      <polygon class="shape-orange" points="180,18 380,18 405,82 380,145 180,145"/>
      <text class="headline" x="197" y="66" font-size="36">30</text>
      <text class="headline" x="241" y="47" font-size="16">%</text>
      <text class="headline" x="242" y="62" font-size="8">Trade Bonus</text>
      <text class="headline" x="197" y="90" font-size="20">For Every</text>
      <text class="headline" x="197" y="110" font-size="20">Trading You</text>
      <text class="headline" x="197" y="129" font-size="20">Make</text>
    </svg>
  </section>

  <section class="banner banner--interest" aria-label="2.5% Annual Interest">
    <div class="banner__photo" role="img" aria-label="Financial line chart printout with a calculator and a red pencil"></div>
    <svg class="banner__art" viewBox="0 0 420 182">
      <polygon class="shape-navy" points="268,0 420,0 420,182 238,182"/>
      <polygon class="shape-fold" points="232,140 262,140 250,162"/>
      <polygon class="shape-orange" points="180,15 380,15 405,78 380,140 180,140"/>
      <text class="headline" x="210" y="68" font-size="34">2.50</text>
      <text class="headline" x="293" y="50" font-size="14">%</text>
      <text class="headline" x="210" y="93" font-size="15">Annual Interest</text>
      <text class="headline" x="210" y="113" font-size="15">For Each of You</text>
    </svg>
  </section>

</main>
</body>
</html>
```